Business Card for a new businees.

need a very good business for a new company based in Riverside California call Levy Lantern LLC. We help client file taxes, resolve tax debt and attain peace of mind We help people nationwide solve Tax problems. We help with Installment agreements, Offers in Compromise, Partial Pay Installment Agreements, Currently Not Collectible status, Liens and Levy Removal, Garnishment removal. We offer individualized services

Target Market(s)

Any one with Tax Problems nationwide. My clients span across age, occupation etc

Contact Information for Business Card

Card must be attractive and have enough information to let client know we care and call us

Colors

Designer to choose colors to be used in the design.

Requirements
Must have
• the basics and then surprise me
Nice to have
• surprise m

```html
<!DOCTYPE html>
<html lang="en">
<head>
<meta charset="utf-8">
<title>Levy Lantern LLC — Business Card</title>
<link rel="stylesheet" href="https://fonts.googleapis.com/css2?family=Open+Sans:wght@400;600;700&display=swap">
<style>
  :root {
    --bg: #141414;
    --card: #1b1b1b;
    --card-edge: #262626;
    --gold: #f2cd1e;
    --gold-deep: #c9a514;
    --text-light: #e6e6e6;
    --text-muted: #b9b9b9;
    --rule: #5a5a5a;
  }
  * { box-sizing: border-box; margin: 0; padding: 0; }
  html, body {
    width: 1200px; height: 900px; overflow: hidden;
    background: var(--bg);
    font-family: "Open Sans", Arial, sans-serif;
  }
  .stage {
    width: 1200px; height: 900px;
    display: flex; flex-direction: column; align-items: center; justify-content: center;
    gap: 60px;
  }
  .card {
    position: relative;
    width: 620px; height: 340px;
    background: var(--card);
    border: 1px solid var(--card-edge);
    border-radius: 22px;
    box-shadow: 0 20px 40px rgba(0,0,0,.5);
  }
  .brand {
    display: flex; flex-direction: column; align-items: flex-start;
  }
  .brand-row { display: flex; align-items: center; gap: 12px; }
  .brand-dot {
    width: 26px; height: 26px; border-radius: 50%;
    background: var(--gold);
  }
  .brand-name {
    color: var(--gold); font-weight: 700; font-size: 38px; letter-spacing: -.5px; line-height: 1;
  }
  .brand-rule {
    width: 100%; height: 3px; background: var(--gold); margin: 8px 0 6px;
  }
  .brand-tagline {
    color: var(--text-light); font-size: 9px; font-weight: 600; letter-spacing: 2.4px;
  }
  .brand-subline {
    color: var(--gold-deep); font-size: 7px; letter-spacing: .6px; margin-top: 3px;
  }
  .card--front .brand {
    position: absolute; left: 50%; top: 50%; transform: translate(-50%, -50%);
  }
  .card--back .brand {
    position: absolute; right: 48px; top: 40px;
  }
  .divider {
    position: absolute; left: 290px; right: 40px; top: 175px;
    height: 1px; background: var(--rule);
  }
  .contact {
    position: absolute; right: 40px; top: 192px;
    list-style: none; display: flex; flex-direction: column; gap: 4px; align-items: flex-end;
  }
  .contact li {
    display: flex; align-items: center; gap: 8px;
    color: var(--text-light); font-size: 16px;
  }
  .contact svg { width: 15px; height: 15px; }
  .person { position: absolute; left: 44px; bottom: 40px; }
  .person-name { color: var(--gold); font-weight: 700; font-size: 22px; }
  .person-role { color: var(--text-muted); font-size: 17px; margin-top: 2px; }
</style>
</head>
<body>
<main class="stage">
  <section class="card card--front" aria-label="Card front">
    <div class="brand">
      <div class="brand-row">
        <span class="brand-dot"></span>
        <span class="brand-name">Levy Lantern</span>
      </div>
      <div class="brand-rule"></div>
      <div class="brand-tagline">TAX SOLUTIONS. TAX FILING.</div>
      <div class="brand-subline">YOUR TAX REPRESENTATIVES, WE ARE TAX EVERYTHING</div>
    </div>
  </section>

  <section class="card card--back" aria-label="Card back">
    <div class="brand">
      <div class="brand-row">
        <span class="brand-dot"></span>
        <span class="brand-name">Levy Lantern</span>
      </div>
      <div class="brand-rule"></div>
      <div class="brand-tagline">TAX SOLUTIONS. TAX FILING.</div>
      <div class="brand-subline">YOUR TAX REPRESENTATIVES, WE ARE TAX EVERYTHING</div>
    </div>

    <div class="divider"></div>

    <ul class="contact">
      <li>044 555 2417
        <svg viewBox="0 0 16 16" aria-hidden="true"><path fill="#f2cd1e" d="M3.5 1.5l2.5 0 1 3.5-1.6 1.2a9 9 0 0 0 4.4 4.4L11 9l3.5 1v2.5a2 2 0 0 1-2 2A11 11 0 0 1 1.5 3.5a2 2 0 0 1 2-2z"/></svg>
      </li>
      <li>hello@levylantern.com
        <svg viewBox="0 0 16 16" aria-hidden="true"><rect x="1" y="3" width="14" height="10" rx="1" fill="#f2cd1e"/><path d="M1.5 3.5L8 9l6.5-5.5" fill="none" stroke="#1b1b1b" stroke-width="1.3"/></svg>
      </li>
      <li>www.levylantern.com
        <svg viewBox="0 0 16 16" aria-hidden="true"><circle cx="8" cy="8" r="7" fill="#f2cd1e"/><path d="M1 8h14M8 1c-3 3.5-3 10.5 0 14M8 1c3 3.5 3 10.5 0 14" fill="none" stroke="#1b1b1b" stroke-width="1"/></svg>
      </li>
    </ul>

    <div class="person">
      <div class="person-name">Marcus Ellery</div>
      <div class="person-role">Managing Director</div>
    </div>
  </section>
</main>
</body>
</html>
```